Hadley & Partners, LLC Business Card 2016

We need a new business card design for a very important trade show coming up.

We are a compliance Consulting Firm. Our clients are stock brokerage firms and investment advisers.

I would like our logo on both sides of the card.

Info in the front of the card shold include:

Logo
First & Last Name
Title
Office #
Cell #
Email
Company Address (42 W. Calloway St., Suite 300 Pasadena, CA 91417

Back of the card should include the logo and url: www.hadleypartnersgroup.com

Target Market(s)

Stock Brokerage Firms and Investment Advisers

Industry/Entity Type

Financial Service

Contact Information for Business Card

Marcus J. Pellew
President
42 W. Calloway St., Suite 300
Pasadena, CA 91417
O 626.555.0147 ext. 204
C 818.555.0193
Email: marcus@hadleypartnersgroup.com
www.hadleypartnersgroup.com

Requirements
Nice to have
• The back of the card could be black with the logo with the white letters.
• I do want the front of the card to at least have the color logo with the black "Hadley & Partners Lettering.

```html
<!DOCTYPE html>
<html lang="en">
<head>
<meta charset="utf-8">
<title>Hadley &amp; Partners — Business Card</title>
<link href="https://fonts.googleapis.com/css2?family=Open+Sans:wght@400;600&display=swap" rel="stylesheet">
<style>
  :root {
    --stage: #3a3a3c;
    --card-white: #ffffff;
    --card-black: #050505;
    --brand-red: #9e1b22;
    --ink: #1a1a1a;
    --divider: #b5b5b5;
    --on-dark: #ffffff;
    --on-dark-soft: #d9d9d9;
  }
  * { box-sizing: border-box; margin: 0; padding: 0; }
  html, body {
    width: 1200px; height: 900px; overflow: hidden;
    background: var(--stage);
    font-family: "Open Sans", Arial, sans-serif;
  }
  .stage { position: relative; width: 1200px; height: 900px; }
  .card {
    position: absolute; left: 250px; width: 700px; height: 400px;
    box-shadow: 0 10px 30px rgba(0,0,0,.45);
    overflow: hidden;
  }
  /* Back side */
  .card--back { top: 35px; background: var(--card-black); }
  .card--back .wordmark {
    position: absolute; left: 150px; top: 130px;
    display: flex; align-items: center; gap: 18px;
  }
  .wordmark__square { width: 46px; height: 46px; background: var(--brand-red); flex: none; }
  .wordmark__name { white-space: nowrap; }
  .card--back .wordmark__name {
    color: var(--on-dark); font-size: 38px; font-weight: 600; letter-spacing: 2px;
  }
  .card--back .back-url {
    position: absolute; left: 150px; top: 250px;
    color: var(--on-dark-soft); font-size: 20px; letter-spacing: .5px;
  }
  /* Front side */
  .card--front { top: 465px; background: var(--card-white); }
  .card--front .wordmark {
    position: absolute; left: 36px; top: 152px;
    display: flex; align-items: center; gap: 10px;
  }
  .card--front .wordmark__square { width: 26px; height: 26px; }
  .card--front .wordmark__name {
    color: var(--ink); font-size: 21px; font-weight: 600; letter-spacing: .5px;
  }
  .front-divider {
    position: absolute; left: 340px; top: 40px; width: 1px; height: 280px;
    background: linear-gradient(to bottom, transparent, var(--divider) 30%, var(--divider) 70%, transparent);
  }
  .contact {
    position: absolute; left: 368px; top: 62px; color: var(--ink);
    font-size: 17px; line-height: 1.35;
  }
  .contact__name { color: var(--brand-red); font-size: 27px; line-height: 1.15; }
  .contact__title { font-size: 18px; margin-bottom: 6px; }
  .contact__address { margin-bottom: 4px; }
  .contact__line { display: flex; align-items: center; gap: 10px; }
  .contact__line svg { width: 14px; height: 14px; flex: none; fill: var(--brand-red); }
  .front-band {
    position: absolute; left: 0; bottom: 0; width: 100%; height: 12px;
    background: linear-gradient(to bottom, var(--brand-red), #7a1218);
  }
</style>
</head>
<body>
<main class="stage">

  <section class="card card--back" aria-label="Card back">
    <div class="wordmark">
      <span class="wordmark__square"></span>
      <span class="wordmark__name">HADLEY &amp; PARTNERS</span>
    </div>
    <p class="back-url">www.hadleypartnersgroup.com</p>
  </section>

  <section class="card card--front" aria-label="Card front">
    <div class="wordmark">
      <span class="wordmark__square"></span>
      <span class="wordmark__name">HADLEY &amp; PARTNERS</span>
    </div>
    <div class="front-divider"></div>
    <div class="contact">
      <p class="contact__name">Marcus J. Pellew</p>
      <p class="contact__title">President</p>
      <p class="contact__address">42 W. Calloway St., Suite 300<br>Pasadena, CA 91417</p>
      <p class="contact__line">
        <svg viewBox="0 0 16 16" aria-hidden="true"><path d="M3.6 1.2l2.3 2.6-1.3 1.8c.9 2 2.6 3.8 4.7 4.8l1.8-1.3 2.6 2.3-1.4 2.4C7 13.4 2.6 9 1.2 3z"/></svg>
        626.555.0147 ext. 204
      </p>
      <p class="contact__line">
        <svg viewBox="0 0 16 16" aria-hidden="true"><path d="M4 0h8a1 1 0 011 1v14a1 1 0 01-1 1H4a1 1 0 01-1-1V1a1 1 0 011-1zm1 2v10h6V2zm3 11a1 1 0 100 2 1 1 0 000-2z"/></svg>
        818.555.0193
      </p>
      <p class="contact__line">
        <svg viewBox="0 0 16 16" aria-hidden="true"><path d="M0 3h16v10H0zm1.5 1.2L8 9l6.5-4.8V4h-13z"/></svg>
        marcus@hadleypartnersgroup.com
      </p>
      <p class="contact__line">
        <svg viewBox="0 0 16 16" aria-hidden="true"><path d="M8 0a8 8 0 110 16A8 8 0 018 0zm0 1.5c-1 1.2-1.6 3-1.7 5.7h3.4C9.6 4.5 9 2.7 8 1.5zM1.6 7.2h3.2c.1-2 .5-3.7 1.2-5A6.5 6.5 0 001.6 7.2zm0 1.6A6.5 6.5 0 006 13.8c-.7-1.3-1.1-3-1.2-5zm4.7 0c.1 2.7.7 4.5 1.7 5.7 1-1.2 1.6-3 1.7-5.7zm4.9 0c-.1 2-.5 3.7-1.2 5a6.5 6.5 0 004.4-5zm3.2-1.6A6.5 6.5 0 0010 2.2c.7 1.3 1.1 3 1.2 5z"/></svg>
        www.hadleypartnersgroup.com
      </p>
    </div>
    <div class="front-band"></div>
  </section>

</main>
</body>
</html>
```